Website Home Page for Women's Health Medical Office

Redesign existing homepage for website using existing logo. Current website location is www.lumawomenscare.com. Please give it a modern, streamlined, playful feel.

Please give it a feminine feel and make it bright and cheerful using logo colors.

Target Market(s)

Women between the ages of 25-45

Industry/Entity Type

Medical Office

Coding

Coded - Design and coding required

Number of Pages Required

1 page

Font styles to use
Sans Serif
Other font styles liked:
• SEGOI UI script for text and GIL SANS for bold (or their equivilent)

Colors
E54698
E96AAD
F1A4CE
F9D9EA
FCEFF6

Requirements
Must have
• Existing logo. Logo Colors. Feminine, cheerful, simple design. all relevant contact information
Nice to have
• clean lines and streamlined look
Should not have
• Cluttered

```html
<!DOCTYPE html>
<html lang="en">
<head>
<meta charset="utf-8">
<title>Luma Women's Care – Home</title>
<link href="https://fonts.googleapis.com/css2?family=Cabin:wght@500;600;700&family=Open+Sans:ital,wght@0,400;0,600;1,400&display=swap" rel="stylesheet">
<style>
:root{
  --pink:#E54698;
  --pink-mid:#E96AAD;
  --pink-soft:#F1A4CE;
  --pink-pale:#F9D9EA;
  --pink-mist:#FCEFF6;
  --ink:#222;
  --text:#555;
}
*{box-sizing:border-box;margin:0;padding:0}
html,body{width:1200px;height:2476px;overflow:hidden}
body{position:relative;font-family:"Open Sans",sans-serif;color:var(--text);background:#fff;font-size:13.5px}
.abs{position:absolute}
h1,h2,h3,.brand-name{font-family:"Cabin",sans-serif;color:var(--ink)}
.icon-ring{width:36px;height:36px;border:1.5px solid var(--pink-mid);border-radius:50%;display:flex;align-items:center;justify-content:center}
.icon-ring svg{width:18px;height:18px;fill:none;stroke:var(--pink);stroke-width:1.6;stroke-linecap:round;stroke-linejoin:round}
/* top bar */
.topbar .item{position:absolute;top:14px;display:flex;align-items:center;gap:12px;font-size:12.5px;color:var(--ink);line-height:1.55}
.topbar .item strong{font-weight:600}
/* nav */
.nav{top:67px;left:0;width:1200px;height:45px;background:var(--pink)}
.nav a{position:absolute;top:14px;color:#fff;text-decoration:none;font-size:13.5px;letter-spacing:.2px}
.logo-badge{left:530px;top:10px;width:140px;height:140px;border-radius:50%;background:#fff;box-shadow:0 0 0 4px var(--pink-pale);display:flex;flex-direction:column;align-items:center;justify-content:center;text-align:center}
.logo-badge .dot{width:34px;height:34px;border-radius:50%;border:1.5px solid var(--pink);margin-bottom:8px}
.brand-name{font-size:15px;font-weight:700;color:var(--ink);line-height:1.1}
/* hero */
.hero{top:112px;left:0;width:1200px;height:525px;background:linear-gradient(115deg,#fbf3f4 0%,#f8e6ea 35%,#fbd9d2 52%,#f9e8ee 70%,#f7ebf3 100%)}
.hero h1{left:62px;top:142px;font-size:50px;line-height:61px;font-weight:700}
.hero .lead{left:62px;top:270px;width:420px;font-size:13.5px;line-height:22px}
.btn{display:inline-block;background:var(--pink);color:#fff;border-radius:20px;font-size:14px;padding:9px 18px;text-decoration:none}
.hero .btn{left:60px;top:357px}
.photo{border-radius:2px}
.hero .model{left:490px;top:72px;width:230px;height:453px;background:linear-gradient(180deg,#f3d3cf 0%,#f1ece9 35%,#e9e6e4 80%,#c9d3df 100%);border-radius:110px 110px 0 0}
.hero .consult{left:819px;top:131px;width:240px;height:150px;background:linear-gradient(135deg,#eef0ee,#c9d0cf 60%,#5f7c86)}
.hero .note-title{left:821px;top:294px;width:250px;font-size:13.5px;font-weight:600;color:var(--ink);line-height:22px}
.hero .note{left:821px;top:345px;width:260px;font-size:13.5px;line-height:22px}
/* framed images */
.frame-shadow{background:var(--pink)}
/* welcome */
.welcome-shadow{left:68px;top:729px;width:362px;height:336px}
.welcome-img{left:60px;top:721px;width:362px;height:336px;background:radial-gradient(ellipse at 55% 40%,#d8b9a6 0%,#6d6f86 40%,#3a4360 100%)}
.welcome h2{left:486px;top:722px;width:520px;font-size:31px;line-height:41px;font-weight:700}
.welcome .body{left:486px;top:808px;width:520px;font-size:13.5px;line-height:22.5px}
.body p+p{margin-top:10px}
/* patients */
.patients h2{left:62px;top:1175px;font-size:29px;font-weight:700}
.patients .body{left:62px;top:1221px;width:520px;font-size:13.5px;line-height:22.5px}
.patients .body p+p{margin-top:6px}
.patients .btn{left:60px;top:1469px}
.patients .call{left:272px;top:1477px;font-size:13.5px}
.patients .call a{color:var(--pink)}
.patients-shadow{left:670px;top:1156px;width:461px;height:396px}
.patients-img{left:678px;top:1147px;width:462px;height:396px;background:linear-gradient(120deg,#ececec 0%,#f2ddd2 45%,#c7d4e6 75%,#9c6a4e 100%)}
/* services */
.services{top:1633px;left:0;width:1200px;height:525px;background:linear-gradient(100deg,#fbeef3 0%,#f9e2e6 30%,#fbd6cb 50%,#f9e7ee 70%,#fbeef4 100%)}
.services .label{left:0;top:56px;width:1260px;text-align:center;font-style:italic;color:var(--pink);font-size:15px}
.services h2{left:0;top:82px;width:1200px;text-align:center;font-size:30px;font-weight:700}
.card{position:absolute;top:142px;width:251px;text-align:center}
.card .pic{height:187px}
.card h3{margin-top:14px;font-size:17px;font-weight:700}
.card p{margin:8px auto 0;width:236px;font-size:13.5px;line-height:22.5px;color:#666}
.card a{display:block;margin-top:10px;color:var(--pink);text-decoration:none;font-size:14px}
/* footer */
.footer{top:2158px;left:0;width:1200px;height:282px;background:var(--pink-mist)}
.footer .brand{left:60px;top:56px;width:210px;height:140px;display:flex;flex-direction:column;align-items:center;justify-content:center;text-align:center}
.footer .brand .dot{width:60px;height:60px;border-radius:50%;border:1.5px solid var(--pink);margin-bottom:12px}
.footer .brand .brand-name{font-size:22px}
.footer h4{font-weight:400;font-size:13px;color:var(--ink);padding-bottom:6px;position:relative}
.footer h4::after{content:"";position:absolute;left:0;bottom:0;width:22px;height:1.5px;background:var(--pink)}
.sitemap{left:337px;top:58px}
.sitemap ul{list-style:none;margin-top:20px}
.sitemap li{font-size:12px;color:var(--ink);margin-bottom:14.5px}
.contact{left:614px;top:58px}
.contact .row{display:flex;align-items:center;gap:16px;font-size:12px;color:var(--ink);margin-top:14px;line-height:1.6}
.contact .row svg{width:20px;height:20px;fill:none;stroke:var(--pink);stroke-width:1.5;stroke-linecap:round;stroke-linejoin:round}
.contact .row strong{font-weight:600}
.follow{left:889px;top:58px}
.socials{display:flex;gap:13px;margin-top:20px}
.socials span{width:30px;height:30px;border:1.5px solid var(--pink);border-radius:50%;display:flex;align-items:center;justify-content:center}
.socials span i{width:10px;height:10px;background:var(--pink);border-radius:50%}
.copyright{left:0;top:2440px;width:1200px;height:36px;background:var(--pink);color:#fff;font-size:12px;text-align:center;line-height:36px}
</style>
</head>
<body>

<header class="topbar">
  <div class="item" style="left:58px"><span class="icon-ring"><svg viewBox="0 0 24 24"><path d="M12 21s-6-6-6-11a6 6 0 0 1 12 0c0 5-6 11-6 11z"/><circle cx="12" cy="10" r="2.2"/></svg></span><span>4180 Willow Crest Drive, Suite 120,<br>Fairhaven, CA 90210</span></div>
  <div class="item" style="left:329px;top:17px"><span class="icon-ring"><svg viewBox="0 0 24 24"><rect x="3" y="6" width="18" height="12" rx="1"/><path d="M3 7l9 6 9-6"/></svg></span><span>hello@lumawomenscare.com</span></div>
  <div class="item" style="left:743px;top:17px"><span class="icon-ring"><svg viewBox="0 0 24 24"><path d="M6 3l3 4-2 2a11 11 0 0 0 8 8l2-2 4 3-2 3C10 21 3 14 3 5z"/></svg></span><strong>(555) 214-3080</strong></div>
  <div class="item" style="left:925px;top:17px"><span class="icon-ring"><svg viewBox="0 0 24 24"><rect x="4" y="9" width="16" height="11" rx="1"/><rect x="8" y="4" width="8" height="5"/><path d="M8 13h2M12 13h2M8 16h2M12 16h2"/></svg></span><strong>555-214-3091</strong></div>
</header>

<nav class="abs nav">
  <a style="left:142px">HOME</a>
  <a style="left:258px">ABOUT US</a>
  <a style="left:389px">SERVICES</a>
  <a style="left:754px">RESOURCES</a>
  <a style="left:910px">CONTACT US</a>
</nav>

<section class="abs hero">
  <h1 class="abs">Better Health<br>Starts Here!</h1>
  <p class="abs lead">Caring for women through every stage of life, with time to listen and explain.</p>
  <a class="abs btn">Schedule An Appoinment</a>
  <div class="abs model photo" role="img" aria-label="Photo of a smiling pregnant woman in a white shirt"></div>
  <div class="abs consult photo" role="img" aria-label="Photo of a doctor consulting with a patient, both wearing masks"></div>
  <p class="abs note-title">Personal care from a team that truly listens.</p>
  <p class="abs note">Every visit is tailored to your needs and questions.</p>
</section>

<div class="abs logo-badge">
  <span class="dot"></span>
  <span class="brand-name">Luma Women's Care</span>
</div>

<section class="welcome">
  <div class="abs frame-shadow welcome-shadow"></div>
  <div class="abs welcome-img photo" role="img" aria-label="Portrait of a smiling doctor in navy scrubs"></div>
  <h2 class="abs">Welcome to Luma Women's Care,<br>Fairhaven, CA</h2>
  <div class="abs body">
    <p>At Luma Women's Care in Fairhaven, California, we believe better health starts when the patient is educated. For this reason, we take time to listen to our patients concerns, explain each option available, and to answer any questions our patients may have so that they can make informed decisions. At Luma Women's Care, our providers tailor every procedure performed and treatment option recommended to meet the specific needs of our patients. We remain up-to-date on the latest technology and practice guidelines for women's health.</p>
    <p>Our medical providers will take time to give you the personalized health care you deserve. This includes taking time to listen to you and screening you for problems to help ensure that any health issues are diagnosed and treated as early as possible.</p>
  </div>
</section>

<section class="patients">
  <h2 class="abs">Now Accepting New Patients</h2>
  <div class="abs body">
    <p>Luma Women's Care offers you the best care possible in a personalized setting. We are currently accepting patients. Call our office now to make an appointment.</p>
    <p>Luma Women's Care (located near Fairhaven Valley Hospital in Fairhaven, CA) is a medical office that specializes in Christ-centered healthcare for women of all ages. Our team of exclusively female providers have years of experience taking care of women with a variety of pregnancy and gynecology concerns.</p>
    <p>Whether you need a routine examination, help during your pregnancy, have questions on birth control, or another female concern, we offer the best care possible for our patients. That is why better health starts here.</p>
  </div>
  <a class="abs btn">Schedule An Appoinment</a>
  <p class="abs call">OR Call Us At <a>(555) 214-3080</a></p>
  <div class="abs frame-shadow patients-shadow"></div>
  <div class="abs patients-img photo" role="img" aria-label="Photo of a mother holding her sleeping newborn"></div>
</section>

<section class="abs services">
  <p class="abs label">Health Services Offered</p>
  <h2 class="abs">How Can We Help You?</h2>
  <article class="card" style="left:60px">
    <div class="pic" role="img" aria-label="Photo of a pregnant woman in a white top" style="background:linear-gradient(180deg,#f6f6f6,#ece6e2 60%,#9fb2c8)"></div>
    <h3>Pregnancy Care</h3>
    <p>Receiving regular care in pregnancy is important for the health of both you and your baby.</p>
    <a>Learn More</a>
  </article>
  <article class="card" style="left:339px">
    <div class="pic" role="img" aria-label="Photo of a woman holding a glass of water and a pill" style="background:linear-gradient(135deg,#e9e6e1,#cdbfb2 55%,#6d4a3a)"></div>
    <h3>Birth Control</h3>
    <p>Our gynecologists are knowledgeable on all forms of birth controlincluding the IUD, the arm implant.</p>
    <a>Learn More</a>
  </article>
  <article class="card" style="left:614px">
    <div class="pic" role="img" aria-label="Photo of a doctor listening to a patient with a stethoscope" style="background:linear-gradient(120deg,#f3efe9,#c26a3c 45%,#e9e7e6 70%,#2f2f2f)"></div>
    <h3>Well Woman Exams</h3>
    <p>Our providers will help you to stay healthy by performing a physical exam on you annually.</p>
    <a>Learn More</a>
  </article>
  <article class="card" style="left:889px">
    <div class="pic" role="img" aria-label="Photo of a patient talking with a doctor at a desk" style="background:linear-gradient(120deg,#dcdcd8,#f2c9c2 40%,#eef0f3 70%,#b86a45)"></div>
    <h3>Women's Health</h3>
    <p>Whether you are dealing with painful or irregular periods, fibroids, or other women's health.</p>
    <a>Learn More</a>
  </article>
</section>

<footer class="abs footer">
  <div class="abs brand">
    <span class="dot"></span>
    <span class="brand-name">Luma Women's Care</span>
  </div>
  <div class="abs sitemap">
    <h4>Site Map</h4>
    <ul><li>HOME</li><li>ABOUT US</li><li>SERVICES</li><li>RESOURCES</li><li>CONTACT US</li></ul>
  </div>
  <div class="abs contact">
    <h4>Contact Us</h4>
    <div class="row" style="margin-top:20px"><svg viewBox="0 0 24 24"><path d="M12 21s-6-6-6-11a6 6 0 0 1 12 0c0 5-6 11-6 11z"/><circle cx="12" cy="10" r="2.2"/></svg><span>4180 Willow Crest Drive, Suite 120,<br>Fairhaven, CA 90210</span></div>
    <div class="row"><svg viewBox="0 0 24 24"><rect x="3" y="6" width="18" height="12" rx="1"/><path d="M3 7l9 6 9-6"/></svg><span>hello@lumawomenscare.com</span></div>
    <div class="row"><svg viewBox="0 0 24 24"><path d="M6 3l3 4-2 2a11 11 0 0 0 8 8l2-2 4 3-2 3C10 21 3 14 3 5z"/></svg><strong>(555) 214-3080</strong></div>
    <div class="row"><svg viewBox="0 0 24 24"><rect x="4" y="9" width="16" height="11" rx="1"/><rect x="8" y="4" width="8" height="5"/><path d="M8 13h2M12 13h2M8 16h2M12 16h2"/></svg><strong>555-214-3091</strong></div>
  </div>
  <div class="abs follow">
    <h4>Follow On Us:</h4>
    <div class="socials" aria-label="Social links"><span><i></i></span><span><i></i></span><span><i></i></span><span><i></i></span></div>
  </div>
</footer>

<div class="abs copyright">Copyright ©2022 Luma Women's Care. All Rights Reserved.</div>

</body>
</html>
```